Hdmi 4K solution Hidden cable solution for wall hung TV, Flyer

VALPEX is an audio visual company that install cabling into new construction of homes.

Design Objective:
Design a 1-Page flyer on a dark background that needs to represent today's latest picture quality and sound solution. This flyer will be in a take home pack with all other components of a new home build (like, bathrooms, paint colour, carpets, flooring, window furnishing ETC) for clients to choose in the design process of building a new home

- I would like this to look as professional as possible and to stand out once clients Turn to our HDMI flyer.

Would like to see the following CONTENTS on the flyer:
- 4k symbol plus VALPEX logo
- "Brimz" brand Logo voted best quality by intergation experts 2015-16-17-18
- image of a TV mounted on a wall representing a wall hung TV with a line diagram behind it (like seeing through the wall) indicating the cable behind the wall (Tesbrin,dry wall )
- photo attached of a sample input

- Automated, Easy
- No clutter or dangling cables on the wall
- 4k guarantee

- Clean, hidden cables. Easy,
- Fully Tested and ready to go
- Just Plug in and way go DIY When you move in to your home
-Product is used in the following rooms:
* Home theatre
* Dining / living room
* Fire place
* Alfresco cabana
* Pool house
* Office

"Choosing the right HDMI Cable to prewire hasn't been easier"

Aesthetics or Preferred Style:
Looking for life style Sound lounge feel in the flyer (please check attached sample brochure and flyer)

Logo is supplied and would like to keep it somewhere in the flyer please. It has sentimental significance.

Actual photo attached of the product ( HDMI) Input and output)

Target Market(s)

New home buyers upgrading accessories in design studios. This product need to be easily identified as inexperienced sales people are usually selling these in display studios. Represent today's latest version of HDMI and fun clear defining tones/colors and picture. Looking for elegant and professional colours /aesthetics

Other font styles liked:
• see attachments

Requirements
Must have
• This flyer will be in a take home pack with all other components of a new home build ex. bathrooms, paint colour, carpets, flooring, window furnishing ETC for clients to choose in the design process of building a new home.
• I would like this to look as professional as possible and to stand out once clients Turn to our HDMI flyer.
Nice to have
• Elegant feel with dark tones to help bridge the professional finish we do from day to day on site on new homes.
• Easy to read ond captivating to choose the HDMI solution to be installed into the new home
Should not have
• I am happy to try something new and not pedestrian or similar to other people as we have pioneered this type of installation package.

```html
<!DOCTYPE html>
<html lang="en">
<head>
<meta charset="utf-8">
<title>Choosing the Right HDMI Cable – Brimz &amp; VALPEX</title>
<link rel="stylesheet" href="https://fonts.googleapis.com/css2?family=Jost:wght@400;500;600&family=Nunito+Sans:wght@400;600&display=swap">
<style>
  :root{
    --navy:#1b3d8a;
    --blue:#1f86c2;
    --sky:#2f7fc1;
    --orange:#f29a2e;
    --orange-deep:#e5572b;
    --yellow:#f8c52c;
    --ink:#333;
    --grey:#5a5a5a;
    --paper:#ffffff;
  }
  *{margin:0;padding:0;box-sizing:border-box}
  html,body{width:848px;height:1200px;overflow:hidden;background:var(--paper)}
  .flyer{position:relative;width:848px;height:1200px;overflow:hidden;background:var(--paper);font-family:"Nunito Sans",sans-serif}
  .artwork{position:absolute;inset:0;width:848px;height:1200px}
  .headline{position:absolute;left:52px;top:566px;font-family:"Jost",sans-serif;font-weight:500;font-size:39px;line-height:38.6px;text-transform:uppercase;
    background:linear-gradient(90deg,var(--navy),var(--blue));-webkit-background-clip:text;background-clip:text;color:transparent}
  .headline .accent{font-weight:600;background:linear-gradient(90deg,var(--orange-deep),var(--yellow));-webkit-background-clip:text;background-clip:text;color:transparent}
  .rule{position:absolute;left:52px;top:826px;width:241px;height:4px;background:linear-gradient(90deg,var(--navy),var(--blue))}
  .intro{position:absolute;left:50px;top:856px;width:292px;font-size:13.2px;line-height:17.3px;color:var(--grey)}
  .section-title{position:absolute;left:523px;font-family:"Jost",sans-serif;font-size:14.6px;line-height:19px;color:var(--sky);text-transform:uppercase}
  .benefits-title{top:651px}
  .rooms-title{top:832px}
  .list{position:absolute;left:525px;list-style:none;font-size:13.6px;line-height:22.8px;color:var(--ink);width:300px}
  .list li{padding-left:12px;position:relative}
  .list li::before{content:"";position:absolute;left:1px;top:10px;width:4px;height:4px;border-radius:50%;background:var(--ink)}
  .benefits{top:678px}
  .rooms{top:882px}
  .brand{position:absolute;left:52px;top:1052px;font-family:"Jost",sans-serif;font-weight:400;font-size:34px;color:#222}
  .partner-note{position:absolute;left:52px;top:1098px;font-size:12.2px;color:var(--grey)}
  .partner{position:absolute;left:196px;top:1081px;font-family:"Jost",sans-serif;font-weight:600;font-size:21px;color:var(--grey);letter-spacing:.3px}
</style>
</head>
<body>
<main class="flyer">
  <svg class="artwork" viewBox="0 0 1060 1500" aria-hidden="false">
    <defs>
      <linearGradient id="ring" x1="0" y1="0" x2="1" y2="1">
        <stop offset="0" stop-color="#1f86c2"/><stop offset="1" stop-color="#1b3d8a"/>
      </linearGradient>
      <linearGradient id="four-k" x1="0" y1="0" x2="1" y2="0">
        <stop offset="0" stop-color="#e5572b"/><stop offset="1" stop-color="#f8c52c"/>
      </linearGradient>
      <linearGradient id="room-photo" x1="0" y1="0" x2="0" y2="1">
        <stop offset="0" stop-color="#e7e6e3"/><stop offset=".55" stop-color="#c9c6c0"/><stop offset="1" stop-color="#6e6458"/>
      </linearGradient>
      <linearGradient id="faded-room" x1="0" y1="0" x2="1" y2="0">
        <stop offset="0" stop-color="#ffffff"/><stop offset="1" stop-color="#eeeeee"/>
      </linearGradient>
      <radialGradient id="cable-photo" cx=".5" cy=".5" r=".6">
        <stop offset="0" stop-color="#8a8a8a"/><stop offset="1" stop-color="#2a2a2a"/>
      </radialGradient>
      <radialGradient id="braid-photo" cx=".5" cy=".5" r=".6">
        <stop offset="0" stop-color="#b9b2a2"/><stop offset="1" stop-color="#3b3a36"/>
      </radialGradient>
    </defs>

    <rect class="faded-room" x="300" y="470" width="760" height="420" fill="url(#faded-room)" role="img" aria-label="Faded photo of a bright living room with shutters"/>

    <polygon class="room-photo" points="0,0 1010,0 865,440 182,565 0,420" fill="url(#room-photo)" role="img" aria-label="Photo of a wall-hung TV above a dark sideboard with vases and flowers"/>

    <polyline points="0,402 184,566 872,442 1060,72" fill="none" stroke="#1b3d8a" stroke-width="30"/>
    <polyline points="0,446 180,606 900,474 1060,122" fill="none" stroke="#1f86c2" stroke-width="18"/>
    <polyline points="372,604 915,492 1060,168" fill="none" stroke="#f29a2e" stroke-width="22"/>
    <polyline points="860,0 1060,0 1060,40" fill="#1b3d8a" stroke="none"/>

    <polygon points="150,1500 1060,1308 1060,1342 250,1500" fill="#f29a2e"/>
    <polygon points="880,1500 1060,1418 1060,1456 960,1500" fill="#1b3d8a"/>
    <polygon points="915,1420 1060,1385 1060,1402 940,1432" fill="#1f86c2"/>

    <line x1="535" y1="795" x2="535" y2="1195" stroke="url(#ring)" stroke-width="7"/>
    <line x1="535" y1="795" x2="720" y2="690" stroke="#1f86c2" stroke-width="7"/>

    <circle cx="720" cy="690" r="72" fill="#f4f4f4" stroke="url(#ring)" stroke-width="12"/>
    <path d="M700 680 h40 v10 l-5 8 h-30 l-5 -8 z" fill="#222"/>
    <rect x="706" y="684" width="28" height="4" fill="#777"/>

    <circle cx="535" cy="795" r="72" fill="url(#cable-photo)" stroke="url(#ring)" stroke-width="12" role="img" aria-label="Photo of two HDMI cable connectors"/>
    <circle cx="535" cy="990" r="72" fill="url(#braid-photo)" stroke="url(#ring)" stroke-width="12" role="img" aria-label="Photo of a braided HDMI cable"/>

    <circle cx="535" cy="1195" r="72" fill="#ffffff" stroke="url(#ring)" stroke-width="12"/>
    <text x="535" y="1215" text-anchor="middle" font-family="Jost, sans-serif" font-weight="600" font-size="66" fill="url(#four-k)">4K</text>
    <text x="535" y="1236" text-anchor="middle" font-family="Nunito Sans, sans-serif" font-size="15" fill="#222">GUARANTEE</text>
  </svg>

  <h1 class="headline">Choosing<br>the right<br><span class="accent">HDMI cable</span><br>to prewire<br>hasn't been<br>easier</h1>
  <div class="rule"></div>
  <p class="intro">The High Definition HDMI Cable Solution allows you to send your High Definition Audio Video signal from e.g. Home Theatre Room to any other room.</p>

  <h2 class="section-title benefits-title">Why use a good HDMI cable</h2>
  <ul class="list benefits">
    <li>Automated, Easy</li>
    <li>No clutter or dangling cables on the wall</li>
    <li>Clean, hidden cables. Easy,</li>
    <li>Fully Tested and ready to go</li>
    <li>Just Plug in and way go DIY when you<br>move in to your home</li>
  </ul>

  <h2 class="section-title rooms-title">Product is used in the<br>following rooms</h2>
  <ul class="list rooms">
    <li>Home theatre</li>
    <li>Dining / living room</li>
    <li>Fire place</li>
    <li>Alfresco cabana</li>
    <li>Pool house</li>
    <li>Office</li>
  </ul>

  <div class="brand">Brimz</div>
  <p class="partner-note">In partnership with</p>
  <div class="partner">VALPEX</div>
</main>
</body>
</html>
```